Bramblewood Poolworks llc Brochure

We need a creative and colorful "Tri-Fold brochure for our swimming pool remodel and construction company. Bramblewood Poolworks llc. In Atlanta Ga. See our website for ideas, content, and photos. We will edit text and photos after just make sure it is Adobe program file. Www.tarnvellapools.com | I couldn't work the sliders yesterday, please check the brief again. Thank you.

Target Market(s)

High end homeowners in metro Atlanta Georgia usa

Industry/Entity Type

Construction

Font styles to use
Serif

Colors
000000
33a6d7
00a990
f37122
ffffff

Requirements
Must have
• Clean colorful. Creative.
Nice to have
• Use more neutral colors to make the pool photos "pop".
Should not have
• Too many Primary colors in the pallet.

```html
<!DOCTYPE html>
<html lang="en">
<head>
<meta charset="utf-8">
<title>Bramblewood Poolworks llc Tri-Fold Brochure</title>
<link href="https://fonts.googleapis.com/css2?family=Raleway:wght@200;300;400;700&family=Arimo:wght@400;700&display=swap" rel="stylesheet">
<style>
  :root {
    --page: #d9d9db;
    --ink: #121318;
    --ink-soft: #1b1c22;
    --white: #ffffff;
    --teal: #1fb5c9;
    --sky: #1e9fe0;
    --navy-band: #2a44a0;
    --logo: #33a6d7;
    --svc-yellow: #c9b21a;
    --svc-lime: #9fbf1e;
    --svc-green: #3fae49;
    --svc-orange: #f37122;
    --svc-aqua: #00a990;
    --svc-red: #e2502a;
    --svc-blue: #3a5cc8;
  }
  * { box-sizing: border-box; margin: 0; padding: 0; }
  html, body { width: 1200px; height: 800px; overflow: hidden; background: var(--page); }
  body { position: relative; font-family: "Arimo", Arial, sans-serif; }

  .panel { position: absolute; top: 80px; width: 275px; height: 640px; background: var(--ink); overflow: hidden; }
  .panel--cover { left: 50px; }
  .panel--about { left: 325px; }
  .panel--inside-left { left: 600px; }
  .panel--inside-right { left: 875px; }

  .photo { position: absolute; }

  /* Cover */
  .cover-logo { position: absolute; top: 105px; left: 0; width: 100%; text-align: center;
    font-family: "Raleway", sans-serif; font-weight: 700; font-size: 21px; color: var(--logo); }
  .cover-photo { left: 0; top: 190px; width: 100%; height: 450px;
    background: linear-gradient(180deg, #4a3f8a 0%, #5d5aa8 22%, #3d4b56 48%, #2c4a3a 66%, #1fc4c0 82%, #2a2a2a 100%); }
  .cover-kicker { position: absolute; top: 300px; width: 100%; text-align: center; color: var(--white);
    font-size: 11.5px; font-weight: 700; letter-spacing: .5px; line-height: 1.2; }
  .cover-title { position: absolute; top: 330px; width: 100%; text-align: center; color: var(--white);
    font-family: "Raleway", sans-serif; font-weight: 200; font-size: 43px; line-height: 41px; }
  .cover-title .small { font-size: 30px; }

  /* About */
  .about-texture { left: 0; top: 0; width: 100%; height: 150px;
    background: linear-gradient(135deg, #2c2d31, #3d3e42 50%, #232428); }
  .about-thumb { left: 92px; top: 75px; width: 88px; height: 78px; border: 3px solid #55565c;
    background: linear-gradient(135deg, #8a8b90, #2d2e33); }
  .about-heading { position: absolute; top: 180px; left: 22px; right: 16px; color: var(--sky);
    font-family: "Raleway", sans-serif; font-weight: 300; font-size: 33px; line-height: 36px; }
  .about-body { position: absolute; top: 268px; left: 22px; right: 22px; color: var(--white);
    font-size: 8.6px; line-height: 1.4; }
  .about-body p + p { margin-top: 9px; }
  .about-photo { left: 0; top: 495px; width: 100%; height: 125px;
    background: linear-gradient(160deg, #6f6a62 0%, #3aa6a8 40%, #4e7a3c 75%, #6a9a3e 100%); }
  .band-blue { position: absolute; left: 0; bottom: 0; width: 100%; height: 20px; background: var(--navy-band); }

  /* Inside spread */
  .band-teal { position: absolute; left: 0; top: 0; width: 100%; height: 22px; background: var(--teal); }
  .hero-left { left: 0; top: 22px; width: 100%; height: 218px;
    background: linear-gradient(180deg, #10182a 0%, #2c3546 40%, #6b5a44 62%, #2ed2f0 78%, #3a3228 100%); }
  .hero-right { left: 0; top: 0; width: 100%; height: 240px;
    background: linear-gradient(180deg, #0e1626 0%, #33394a 38%, #8a5a2a 60%, #4a3a2a 80%, #2e2a22 100%); }
  .house-pool { left: 0; top: 240px; width: 100%; height: 120px;
    background: linear-gradient(180deg, #2b3b4a 0%, #e9ecef 35%, #7fc8e6 65%, #2b5a86 100%); }
  .kitchen { left: 150px; top: 360px; width: 125px; height: 82px;
    background: linear-gradient(135deg, #8a6a4a, #d9c4a2 55%, #5a4430); }
  .inside-copy { position: absolute; top: 460px; left: 22px; right: 22px; color: var(--white);
    font-size: 8.6px; line-height: 1.4; }
  .spa { left: 0; top: 240px; width: 263px; height: 180px;
    background: linear-gradient(160deg, #3a3a3a 0%, #8a8a86 35%, #5fd0ea 65%, #3e6a3a 100%); }
  .accent-strip { position: absolute; right: 0; top: 300px; width: 12px; height: 120px; background: var(--sky); }

  .services { position: absolute; top: 450px; left: 20px; right: 12px; list-style: none;
    font-size: 17px; line-height: 20px; }
  .services .light { font-weight: 400; }
  .services .bold { font-weight: 700; }
  .svc-yellow { color: var(--svc-yellow); }
  .svc-lime { color: var(--svc-lime); }
  .svc-green { color: var(--svc-green); }
  .svc-orange { color: var(--svc-orange); }
  .svc-aqua { color: var(--svc-aqua); }
  .svc-red { color: var(--svc-red); }
  .svc-blue { color: var(--svc-blue); }
</style>
</head>
<body>

<section class="panel panel--cover">
  <div class="cover-logo">Bramblewood Poolworks llc</div>
  <div class="photo cover-photo" role="img" aria-label="Night view of a backyard pool with stone fireplace, pergola and lit trees"></div>
  <div class="cover-kicker">TARNVELLA POOLS<br>IS YOUR</div>
  <h1 class="cover-title">One Stop<br>Source<br><span class="small">for</span><br>Outdoor<br>Living</h1>
</section>

<section class="panel panel--about">
  <div class="photo about-texture" role="img" aria-label="Dark textured stone backdrop"></div>
  <div class="photo about-thumb" role="img" aria-label="Black and white pool detail photo"></div>
  <h2 class="about-heading">Atlanta Pool<br>Builders</h2>
  <div class="about-body">
    <p>With over 30 years of experience dedicated to creating the highest quality outdoor spaces. We specialize in custom pools with an emphasis on customer service. Tarnvella Pools works to create unique, intuitive designs that show your personal style in an outdoor living space to the fullest.</p>
    <p>We design and build the best pools at a competition price, in a timely manner.</p>
    <p>Serving the metro area including Cumming, Atlanta, Sandy Springs and Gainesville. We take exceptional customer service and the difference is in the details.</p>
  </div>
  <div class="photo about-photo" role="img" aria-label="Garden pool with stone edging and lawn"></div>
  <div class="band-blue"></div>
</section>

<section class="panel panel--inside-left">
  <div class="band-teal"></div>
  <div class="photo hero-left" role="img" aria-label="Lit pool with rock waterfall and slide at dusk"></div>
  <div class="photo house-pool" role="img" aria-label="Modern white house with infinity pool"></div>
  <div class="photo kitchen" role="img" aria-label="Stone outdoor kitchen"></div>
  <p class="inside-copy">Providing design and installation of custom pools and landscapes in as little as 6 to 8 weeks. We will handle your project from concept to completion. We strive to create spaces that add not only beauty but functionality to your existing home. Atlanta pool builders, Tarnvella Pools, wants to help you create a space that is inviting, fun and creates a vacation destination in your backyard.</p>
  <div class="band-blue"></div>
</section>

<section class="panel panel--inside-right">
  <div class="photo hero-right" role="img" aria-label="Covered outdoor pavilion lit at night beside the pool"></div>
  <div class="photo spa" role="img" aria-label="Raised spa spilling into a pool with stone wall"></div>
  <div class="accent-strip"></div>
  <ul class="services">
    <li class="light svc-yellow">Custom Pool Design and Construction</li>
    <li class="bold svc-lime">Pool Renovation and Remodeling</li>
    <li class="light svc-orange">Outdoor Fireplaces</li>
    <li class="bold svc-aqua">Outdoor Kitchens</li>
    <li class="light svc-red">Outdoor Audio and Video</li>
    <li class="bold svc-blue">Low Voltage Lighting</li>
  </ul>
</section>

</body>
</html>
```